Location detection - billboard

Poster / billboard is to be hung in front of the building. When you see the billboard you have to know immediately that here is a location, which company, what we do, based on picture or text, website address.
The main business is professional window tinting. But we also make paint protection film.
It shouldn't be too full, legible but clear
There should be a billboard on the street so people know that there is a location. With logo, performance information and that people are welcome (maybe with a => (here) sign)
Colors should be similar to those on the uploaded images

Target Market(s)

Customers - motorists

Font styles to use
Sans Serif

Requirements
Must have
• My logo must be on it. It must be clear that there is a location here and how to reach us

```html
<!DOCTYPE html>
<html lang="de">
<head>
<meta charset="utf-8">
<title>TINTWERK – Billboards</title>
<link rel="stylesheet" href="https://fonts.googleapis.com/css2?family=Montserrat:wght@500;600;700;800&family=Roboto+Condensed:ital,wght@1,800;1,900&display=swap">
<style>
  :root{
    --red:#ee1c24;
    --gold-light:#f6ec8a;
    --gold:#d9b64a;
    --gold-dark:#b8902a;
    --board:#232323;
    --board-dark:#1a1a1a;
    --board-light:#2b2b2b;
    --white:#ffffff;
    --ink:#111111;
    --page-top:#ffffff;
    --page-bottom:#c4c4c4;
  }
  *{margin:0;padding:0;box-sizing:border-box}
  html,body{width:909px;height:1200px;overflow:hidden}
  body{
    position:relative;
    background:linear-gradient(160deg,var(--page-top) 0%,#ececec 45%,var(--page-bottom) 100%);
    font-family:"Montserrat",Arial,sans-serif;
  }
  .board-title{
    position:absolute;left:0;width:909px;text-align:center;
    font-weight:800;font-size:34px;color:var(--ink);letter-spacing:0.5px;
  }
  .board-title--first{top:51px}
  .board-title--second{top:617px}

  .billboard{
    position:absolute;left:71px;width:768px;height:448px;overflow:hidden;
    background:
      linear-gradient(112deg,transparent 0 60%,rgba(0,0,0,.18) 60% 100%),
      linear-gradient(112deg,var(--board-dark) 0%,var(--board) 22%,var(--board-light) 22%,var(--board) 48%,var(--board-light) 48%,#262626 100%);
    box-shadow:0 14px 22px rgba(0,0,0,.35);
  }
  .billboard--contact{top:113px}
  .billboard--direction{top:682px}

  .brand-name{
    position:absolute;font-weight:700;color:var(--red);line-height:1;letter-spacing:-1px;
  }
  .service-title{
    position:absolute;font-family:"Roboto Condensed",Arial,sans-serif;font-style:italic;font-weight:900;
    font-size:48px;line-height:47px;text-transform:uppercase;letter-spacing:-0.5px;
    background:linear-gradient(180deg,var(--gold-light) 0%,var(--gold) 55%,var(--gold-dark) 100%);
    -webkit-background-clip:text;background-clip:text;color:transparent;
  }

  /* Billboard 1 */
  .billboard--contact .brand-name--headline{left:48px;top:48px;font-size:46px}
  .billboard--contact .service-title{left:48px;top:107px}
  .billboard--contact .brand-name--mark{left:450px;top:98px;width:285px;text-align:center;font-size:44px}
  .address-block{position:absolute;left:48px;top:237px;display:flex;gap:20px;align-items:flex-start}
  .address-block svg{width:38px;height:60px;flex:none}
  .address-block p{color:var(--white);font-weight:500;font-size:23px;line-height:30px;margin-top:3px}
  .tagline{
    position:absolute;left:48px;top:343px;font-family:"Roboto Condensed",Arial,sans-serif;
    font-style:italic;font-weight:900;font-size:34px;line-height:40px;color:var(--red);letter-spacing:-0.3px;
  }
  .contact-panel{position:absolute;left:0;top:0;width:768px;height:448px}
  .contact-list{position:absolute;left:480px;top:290px;width:280px;list-style:none}
  .contact-list li{display:flex;align-items:center;color:var(--ink);font-weight:500;font-size:21px;line-height:27px}
  .contact-list svg{flex:none}
  .contact-email{padding-left:60px;gap:7px}
  .contact-web{padding-left:60px;gap:7px}
  .contact-phone{padding-left:16px;gap:8px;margin-top:8px;color:var(--red)!important;font-weight:700!important;font-size:28px!important;line-height:36px!important}
  .social-row{position:absolute;left:544px;top:398px;display:flex;gap:8px}
  .social-row span{width:23px;height:23px;border-radius:50%;background:#888}
  .social-row span:nth-child(1){background:#3b5998}
  .social-row span:nth-child(2){background:#4c9a52}
  .social-row span:nth-child(3){background:#c13584}
  .social-row span:nth-child(4){background:#e23c3c}

  /* Billboard 2 */
  .billboard--direction .brand-name--mark{left:40px;top:110px;width:290px;text-align:center;font-size:46px}
  .billboard--direction .brand-name--headline{left:355px;top:59px;font-size:46px}
  .billboard--direction .service-title{left:355px;top:116px}
  .direction-arrow{position:absolute;left:0;top:0;width:768px;height:448px}
  .direction-label{
    position:absolute;left:210px;top:262px;width:380px;text-align:center;
    font-family:"Roboto Condensed",Arial,sans-serif;font-style:italic;font-weight:900;
    font-size:60px;line-height:64px;color:var(--white);letter-spacing:2px;
  }
  .direction-address{
    position:absolute;left:96px;top:370px;display:flex;align-items:center;gap:12px;
    color:var(--white);font-weight:500;font-size:28px;line-height:34px;
  }
  .direction-address svg{width:18px;height:26px}
</style>
</head>
<body>

  <h2 class="board-title board-title--first">Billboard 1</h2>
  <section class="billboard billboard--contact">
    <svg class="contact-panel" viewBox="0 0 768 448" aria-hidden="true">
      <path d="M345 448 C300 360 320 240 500 232 C620 228 720 280 768 318 L768 448 Z" fill="#ee1c24"/>
      <path d="M400 448 C352 372 370 262 522 253 C632 248 718 292 768 336 L768 448 Z" fill="#ffffff"/>
    </svg>

    <div class="brand-name brand-name--headline">TINTWERK</div>
    <h1 class="service-title">Professionelle<br>Scheibentönung</h1>
    <div class="brand-name brand-name--mark">TINTWERK</div>

    <div class="address-block">
      <svg viewBox="0 0 38 60" aria-hidden="true">
        <path d="M19 2 C9 2 3 9 3 18 C3 28 12 36 19 50 C26 36 35 28 35 18 C35 9 29 2 19 2 Z" fill="#ee1c24"/>
        <circle cx="19" cy="18" r="7" fill="#232323"/>
        <ellipse cx="19" cy="52" rx="17" ry="6" fill="none" stroke="#ee1c24" stroke-width="3"/>
      </svg>
      <p>Lindenweg 14, 85740<br>Munich Nordheim</p>
    </div>

    <p class="tagline">Window Tinting and<br>Foiling Munich!</p>

    <ul class="contact-list">
      <li class="contact-email">
        <svg width="14" height="10" viewBox="0 0 14 10" aria-hidden="true"><rect x="0.75" y="0.75" width="12.5" height="8.5" fill="none" stroke="#ee1c24" stroke-width="1.3"/><path d="M1 1 L7 6 L13 1" fill="none" stroke="#ee1c24" stroke-width="1.3"/></svg>
        info@tintwerk.de
      </li>
      <li class="contact-web">
        <svg width="14" height="14" viewBox="0 0 14 14" aria-hidden="true"><circle cx="7" cy="7" r="6" fill="none" stroke="#ee1c24" stroke-width="1.3"/><path d="M1 7 H13 M7 1 C3 5 3 9 7 13 M7 1 C11 5 11 9 7 13" fill="none" stroke="#ee1c24" stroke-width="1.1"/></svg>
        www.tintwerk.de
      </li>
      <li class="contact-phone">
        <svg width="22" height="22" viewBox="0 0 22 22" aria-hidden="true"><circle cx="11" cy="11" r="10" fill="none" stroke="#111" stroke-width="1.6"/><path d="M7.5 5.5 L9.5 5.5 L10.3 8.3 L9 9.3 C9.7 11 11 12.3 12.7 13 L13.7 11.7 L16.5 12.5 L16.5 14.5 C16.5 15.4 15.7 16 14.8 15.9 C10.3 15.3 6.7 11.7 6.1 7.2 C6 6.3 6.6 5.5 7.5 5.5 Z" fill="#111"/></svg>
        0151 24680 135
      </li>
    </ul>
    <div class="social-row" aria-label="Social media"><span></span><span></span><span></span><span></span></div>
  </section>

  <h2 class="board-title board-title--second">Billboard 2</h2>
  <section class="billboard billboard--direction">
    <div class="brand-name brand-name--mark">TINTWERK</div>
    <div class="brand-name brand-name--headline">TINTWERK</div>
    <h1 class="service-title">Professionelle<br>Scheibentönung</h1>

    <svg class="direction-arrow" viewBox="0 0 768 448" aria-hidden="true">
      <path d="M100 300 L182 235 L182 267 L673 267 L673 330 L184 330 L184 365 Z" fill="#ffffff"/>
      <path d="M97 297 L179 232 L179 264 L670 264 L670 327 L181 327 L181 362 Z" fill="#ee1c24"/>
    </svg>
    <div class="direction-label">ON THIS WAY</div>

    <p class="direction-address">
      <svg viewBox="0 0 18 26" aria-hidden="true"><path d="M9 1 C4.5 1 2 4 2 8 C2 12 6 15.5 9 21 C12 15.5 16 12 16 8 C16 4 13.5 1 9 1 Z" fill="#ee1c24"/><circle cx="9" cy="8" r="3" fill="#232323"/><ellipse cx="9" cy="22.5" rx="7.5" ry="2.5" fill="none" stroke="#ee1c24" stroke-width="1.5"/></svg>
      Lindenweg 14, 85740 Munich Nordheim
    </p>
  </section>

</body>
</html>
```